Company email signature, make it look perfect!

make my signature high resolution, and ready for use as a outlook email signature
Look at the doc below ' this is what im looking to achieve.
The key items are - make this all high resolution with the actual images below used. Make the signature all the same colour.
If you want to make the signature look better than it does, with the layout below. It has to incorporate everything in the ' this is what im trying to achieve doc'
The order of the brands below 'Forma Construction Group' are to go in the order : Stonerise , Commercial Builders Kestrelton, Kestrelton Renovation builders, builders kestrelton
Forma Construction Group Signature

```html
<!DOCTYPE html>
<html lang="en">
<head>
<meta charset="utf-8">
<title>Forma Construction Group – Email Signature</title>
<link href="https://fonts.googleapis.com/css2?family=Manrope:wght@400;500;700;800&display=swap" rel="stylesheet">
<style>
  :root {
    --ink: #34495a;
    --page: #e8e8e8;
    --card: #ffffff;
    --rule: #4a5d6c;
  }
  * { box-sizing: border-box; margin: 0; padding: 0; }
  html, body {
    width: 1200px; height: 848px; overflow: hidden;
    background: var(--page);
    font-family: "Manrope", Arial, sans-serif;
    color: var(--ink);
  }
  .signature {
    position: absolute; left: 133px; top: 293px;
    width: 963px; height: 240px;
    background: var(--card);
  }
  .sign-off {
    position: absolute; left: 39px; top: 17px;
    font-size: 15px; font-weight: 700;
  }
  .brand {
    position: absolute; left: 101px; top: 58px;
    display: flex; align-items: center; gap: 14px;
  }
  .brand-mark {
    width: 40px; height: 40px; background: var(--ink);
  }
  .brand-name {
    font-size: 25px; font-weight: 500; line-height: 28px;
    text-transform: uppercase; letter-spacing: 0.2px;
  }
  .sister-brands {
    position: absolute; left: 45px; top: 184px;
    width: 415px;
    display: flex; justify-content: space-between; align-items: center;
  }
  .sister-brand {
    font-size: 10px; font-weight: 700; line-height: 11px;
    text-transform: uppercase; text-align: center;
  }
  .divider {
    position: absolute; left: 508px; top: 19px;
    width: 1.5px; height: 203px; background: var(--rule);
  }
  .contact {
    position: absolute; left: 548px; top: 51px;
  }
  .contact-name {
    margin-left: 21px;
    font-size: 18.5px; font-weight: 800; letter-spacing: 0.6px;
    text-transform: uppercase; line-height: 24px;
  }
  .contact-role {
    margin-left: 21px;
    font-size: 17px; font-weight: 400; line-height: 24px;
  }
  .contact-list { list-style: none; margin-top: 19px; }
  .contact-list li {
    display: flex; align-items: center; gap: 10px;
    font-size: 16.4px; font-weight: 700; line-height: 22px;
  }
  .contact-list svg { width: 11px; height: 11px; flex: none; }
</style>
</head>
<body>
  <section class="signature">
    <p class="sign-off">Kind regards</p>

    <div class="brand">
      <span class="brand-mark"></span>
      <span class="brand-name">Forma<br>Construction<br>Group</span>
    </div>

    <div class="sister-brands">
      <span class="sister-brand">Stonerise</span>
      <span class="sister-brand">Commercial<br>Builders<br>Kestrelton</span>
      <span class="sister-brand">Kestrelton<br>Renovation<br>Builders</span>
      <span class="sister-brand">Builders<br>Kestrelton</span>
    </div>

    <span class="divider"></span>

    <div class="contact">
      <p class="contact-name">Daniel Ashcombe</p>
      <p class="contact-role">Managing Director</p>
      <ul class="contact-list">
        <li>
          <svg viewBox="0 0 12 12" aria-hidden="true"><path d="M3 1.5c-1 1-1.8 3 0 5.5s4 4 5.5 4.2c.6 0 1-.4 1.3-.9L8 8.7 6.8 9.4C5.6 8.7 4 7 3.3 5.8L4 4.6 2.9 1.4z" fill="currentColor"/></svg>
          022 555 0187
        </li>
        <li>
          <svg viewBox="0 0 12 12" aria-hidden="true" fill="none" stroke="currentColor" stroke-width="1"><circle cx="6" cy="6" r="5"/><ellipse cx="6" cy="6" rx="2.2" ry="5"/><path d="M1 6h10M2 3.4h8M2 8.6h8"/></svg>
          www.formaconstructiongroup.co.nz
        </li>
        <li>
          <svg viewBox="0 0 12 12" aria-hidden="true" fill="none" stroke="currentColor" stroke-width="1.3"><circle cx="6" cy="6" r="2"/><path d="M8 4v2.6c0 1 1.9 1 2-.6.3-3-2-5-4.6-4.4S1.2 5 2 7.6s4 3.5 6.3 2.3"/></svg>
          daniel@formaconstructiongroup.co.nz
        </li>
      </ul>
    </div>
  </section>
</body>
</html>
```